Personal Card: Make it roar!

Hello to all designers,
Hope you're having a nice day/evening! Let's cut to the chase. I would like a modern, beautiful and professional personal business card; with a vector-art of a lion. I'd like the lion to be Blood Red. On a black background. I'm a Filipino, and would love to have my country's flag incorporated into the design. Id like the stars of my flag to be used in your designs if possible. The texts I want on the card are only my name, number, and email address. Colour of my name should be White, and my details Silver. The size and font should be simple and professional, you're in charge of that! The placements of the lion and my details will be yours to decide.

At the back of the card, I would like just the words "Thank You" (Silver) on a Black Background. Right on the center.

To summarise, my requirements are:
- Blood Red: Front Face of Lion, Vector-Art
- Black: Background
- Yellow: Three Stars used in the design
- White: Bartholomew Sr Pelaez
- Silver: Number & Email (Where appropriate)
- Back of the card (Center). Silver: "Thank You"
- Please DON'T use the colour blue.

It's all about the Lion. Images you'll find attached are some images of Lions' faces which I particularly want to be captured and put onto the card. Convert it into a vector-art. A vector-art Lion. PLEASE use the images attached for inspiration only! Do not use it on your designs. Thank you very much for your time.

Good luck!

Bart

Hello Desginers, Please use Blood Red for the colour red in your designs:HEX: 8A0707RGB: 138,7,7Thank you,Bart Added Saturday, March 12, 2016

Target Market(s)

Potential Connections

Industry/Entity Type

It Professional

Contact Information for Business Card

Name: Bartholomew Sr Pelaez
Email: bartpelaez@zentomail.example
Number: 07391628047

Requirements
Must have
• Modern, Professional & Simple
• (Blood Red HEX: 8A0707, RGB: 138,7,7) Lion (Vector-style art)
• (Black) Background
• (White) My Name
• (Silver) My Details
• Back of card: "Thank You" in Silver. Font size should be small/medium.
• Only colours that should be used are Red, Black, Yellow and White/Silver
Nice to have
• - Use of 3 Yellow stars on the design
Should not have
• - Please avoid using any other colours apart from those specified.

```html
<!DOCTYPE html>
<html lang="en">
<head>
<meta charset="utf-8">
<title>Personal Business Card – Bartholomew Sr Pelaez</title>
<link rel="stylesheet" href="https://fonts.googleapis.com/css2?family=Questrial&family=Karla:wght@400&display=swap">
<style>
  :root {
    --canvas-bg: #e9e4dc;
    --card-black: #000000;
    --lion-red: #d10a0a;
    --star-yellow: #ffe600;
    --name-white: #ffffff;
    --detail-silver: #c9c9c9;
    --card-shadow: rgba(0, 0, 0, 0.35);
  }

  * { box-sizing: border-box; margin: 0; padding: 0; }

  html, body {
    width: 1200px;
    height: 1200px;
    overflow: hidden;
    background: var(--canvas-bg);
  }

  .card-sheet {
    position: relative;
    width: 1200px;
    height: 1200px;
  }

  .card {
    position: absolute;
    left: 150px;
    width: 900px;
    height: 527px;
    background: var(--card-black);
    box-shadow: 0 8px 22px var(--card-shadow);
  }

  .card--front { top: 53px; }
  .card--back  { top: 620px; }

  .star {
    position: absolute;
    width: 30px;
    height: 30px;
  }
  .star--left   { left: 325px; top: 98px; }
  .star--right  { left: 590px; top: 62px; }
  .star--bottom { left: 520px; top: 320px; }

  .lion-art {
    position: absolute;
    left: 385px;
    top: 95px;
    width: 165px;
    height: 205px;
    border-radius: 48% 48% 45% 45% / 40% 40% 60% 60%;
    background: radial-gradient(ellipse at 50% 45%, #3a0202 0%, #7a0505 55%, var(--lion-red) 100%);
  }

  .owner-name {
    position: absolute;
    left: 0;
    right: 0;
    top: 372px;
    text-align: center;
    font-family: "Questrial", sans-serif;
    font-size: 33px;
    color: var(--name-white);
    letter-spacing: 0.2px;
  }

  .contact-line {
    position: absolute;
    left: 0;
    right: 0;
    top: 428px;
    display: flex;
    justify-content: center;
    align-items: center;
    gap: 26px;
    font-family: "Karla", sans-serif;
    font-size: 25px;
    color: var(--detail-silver);
  }

  .contact-item {
    display: flex;
    align-items: center;
    gap: 8px;
  }

  .contact-icon {
    width: 20px;
    height: 20px;
    fill: #8e8e8e;
  }

  .thank-you {
    position: absolute;
    left: 0;
    right: 0;
    top: 50%;
    transform: translateY(-50%);
    text-align: center;
    font-family: "Karla", sans-serif;
    font-size: 24px;
    color: var(--name-white);
    letter-spacing: 0.5px;
  }
</style>
</head>
<body>
<main class="card-sheet">

  <section class="card card--front" aria-label="Card front">
    <svg class="star star--left" viewBox="0 0 24 24" aria-hidden="true">
      <polygon fill="var(--star-yellow)" points="12,1 14.8,8.6 23,8.9 16.5,13.9 18.8,21.8 12,17.2 5.2,21.8 7.5,13.9 1,8.9 9.2,8.6"/>
    </svg>
    <svg class="star star--right" viewBox="0 0 24 24" aria-hidden="true">
      <polygon fill="var(--star-yellow)" points="12,1 14.8,8.6 23,8.9 16.5,13.9 18.8,21.8 12,17.2 5.2,21.8 7.5,13.9 1,8.9 9.2,8.6"/>
    </svg>
    <svg class="star star--bottom" viewBox="0 0 24 24" aria-hidden="true">
      <polygon fill="var(--star-yellow)" points="12,1 14.8,8.6 23,8.9 16.5,13.9 18.8,21.8 12,17.2 5.2,21.8 7.5,13.9 1,8.9 9.2,8.6"/>
    </svg>

    <div class="lion-art" role="img" aria-label="Blood-red line-art illustration of a lion's head facing forward"></div>

    <p class="owner-name">Bartholomew Sr Pelaez</p>

    <div class="contact-line">
      <span class="contact-item">
        <svg class="contact-icon" viewBox="0 0 24 24" aria-hidden="true">
          <path d="M6.6 10.8c1.4 2.8 3.8 5.1 6.6 6.6l2.2-2.2c.3-.3.7-.4 1-.2 1.1.4 2.3.6 3.6.6.6 0 1 .4 1 1V20c0 .6-.4 1-1 1C10.6 21 3 13.4 3 4c0-.6.4-1 1-1h3.5c.6 0 1 .4 1 1 0 1.3.2 2.5.6 3.6.1.3 0 .7-.2 1L6.6 10.8z"/>
        </svg>
        <span class="contact-phone">07391628047</span>
      </span>
      <span class="contact-item">
        <svg class="contact-icon" viewBox="0 0 24 24" aria-hidden="true">
          <path d="M2 5h20v14H2V5zm2 2v.5l8 5.5 8-5.5V7H4zm0 2.9V17h16V9.9l-8 5.5-8-5.5z"/>
        </svg>
        <span class="contact-email">bartpelaez@zentomail.example</span>
      </span>
    </div>
  </section>

  <section class="card card--back" aria-label="Card back">
    <p class="thank-you">Thank You</p>
  </section>

</main>
</body>
</html>
```